Hi, Looking for an upgraded business card to the aged one attached. Open to suggestions and no real limitations, but if your going to use a picture of a taxi i think it should be vector based rather than a full color picture. I've uploaded a 2 pictures of the type of taxi which is a Torvane K5 in white. The taxi markings look like the pink one in the picture but to be clear his is white. The taxi is in Bermuda so if you wanted to include something island based that's ok as well but not required. The other thing he wanted to keep on there was the bermuda police crest, with the retired police office incorporated somehow.

Requirements
Must have
• Bermuda Taxi Operator
Retired Police Officer
Police Crest
Taxi #
Email
Mobile Number

```html
<!DOCTYPE html>
<html lang="en">
<head>
<meta charset="UTF-8">
<title>Bermuda Taxi Operator – Business Card</title>
<link href="https://fonts.googleapis.com/css2?family=Open+Sans:wght@400;800&display=swap" rel="stylesheet">
<style>
  :root {
    --paper: #ffffff;
    --ink: #000000;
    --crest-blue: #1b4f8f;
    --band-orange: #f5a62b;
    --band-dark: #1f1f1f;
  }
  * { margin: 0; padding: 0; box-sizing: border-box; }
  html, body { width: 1200px; height: 706px; overflow: hidden; background: var(--paper); }
  .card {
    position: relative;
    width: 1200px;
    height: 706px;
    background: var(--paper);
    font-family: "Open Sans", Arial, sans-serif;
    color: var(--ink);
    overflow: hidden;
  }
  .card__title {
    position: absolute;
    top: 72px;
    left: 0;
    width: 100%;
    text-align: center;
    font-weight: 800;
    font-size: 66px;
    line-height: 1;
  }
  .operator {
    position: absolute;
    top: 248px;
    left: 188px;
    width: 460px;
    text-align: center;
  }
  .operator__name {
    font-weight: 800;
    font-size: 51px;
    line-height: 1.1;
    white-space: nowrap;
  }
  .operator__role {
    font-weight: 400;
    font-size: 26px;
    margin-top: 6px;
  }
  .emblem {
    position: absolute;
    top: 186px;
    left: 660px;
    width: 216px;
    height: 226px;
    display: flex;
    flex-direction: column;
    align-items: center;
    justify-content: center;
    gap: 12px;
  }
  .emblem__circle {
    width: 150px;
    height: 150px;
    border-radius: 50%;
    background: var(--crest-blue);
  }
  .emblem__name {
    font-weight: 800;
    font-size: 19px;
    color: var(--crest-blue);
    text-align: center;
    white-space: nowrap;
    line-height: 1.15;
  }
  .contact {
    position: absolute;
    top: 440px;
    left: 0;
    width: 1200px;
    text-align: center;
  }
  .contact__line {
    font-weight: 400;
    font-size: 31px;
    line-height: 50px;
  }
  .contact__phone {
    font-weight: 800;
    font-size: 45px;
    line-height: 60px;
    margin-top: 2px;
  }
  .taxi-band {
    position: absolute;
    left: 0;
    bottom: 0;
    width: 1200px;
    height: 83px;
    background: linear-gradient(180deg, var(--band-orange), #c98a2a);
  }
</style>
</head>
<body>
  <div class="card">
    <h1 class="card__title">BERMUDA TAXI OPERATOR</h1>

    <div class="operator">
      <p class="operator__name">Dennis Calloway</p>
      <p class="operator__role">Retired Police Officer</p>
    </div>

    <div class="emblem">
      <div class="emblem__circle"></div>
      <p class="emblem__name">Island Constabulary</p>
    </div>

    <div class="contact">
      <p class="contact__line">Taxi #T2714</p>
      <p class="contact__line">dcalloway52@mailbox.com</p>
      <p class="contact__phone">1-441-555-0147</p>
    </div>

    <div class="taxi-band" role="img" aria-label="Orange and black taxi checker band"></div>
  </div>
</body>
</html>
```